Medical Waste Company with Logo

Need a business card design that targets office managers in the medical community. This card will be the front line for our sales team to market our services to the community. We would like to have email, phone number, website. Please use the logo attached to create a design that we would be proud of.

Target Market(s)

Medical Clients

Industry/Entity Type

Medical Supply

Contact Information for Business Card

Please use logo attached

Colors

Designer to choose colors to be used in the design.

Requirements
Must have
• Our logo (see attached file)
Nice to have
• Maybe a pop of some sort, raised..?

```html
<!DOCTYPE html>
<html lang="en">
<head>
<meta charset="utf-8">
<title>Glacier Clinical Disposal – Business Card</title>
<link href="https://fonts.googleapis.com/css2?family=Montserrat:wght@500;600;700&family=Open+Sans:wght@400;600&display=swap" rel="stylesheet">
<style>
  :root {
    --stage: #2b2b2d;
    --card-black: #0b0b0c;
    --card-white: #ffffff;
    --brand-blue: #1f67a8;
    --silver: #b9bbbe;
    --icon-grey: #8a8c8f;
    --ink-blue: #1f5f9c;
  }
  * { margin: 0; padding: 0; box-sizing: border-box; }
  html, body {
    width: 1200px; height: 902px; overflow: hidden;
    background: var(--stage);
  }
  .stage {
    width: 1200px; height: 902px;
    display: flex; flex-direction: column; align-items: center; justify-content: center;
    gap: 36px;
  }
  .card {
    position: relative;
    width: 700px; height: 400px;
    overflow: hidden;
    box-shadow: 0 10px 30px rgba(0,0,0,.45);
  }

  /* Back side */
  .card-back { background: var(--card-black); }
  .card-back .wordmark {
    position: absolute; left: 0; right: 0; top: 175px;
    font-family: "Montserrat", sans-serif; font-weight: 600;
    font-size: 32px; letter-spacing: 1px;
    color: var(--silver);
    display: flex; align-items: center; justify-content: center; gap: 14px;
  }
  .mark-square {
    width: 20px; height: 20px; background: currentColor; display: inline-block; flex: none;
  }

  /* Front side */
  .card-front { background: var(--card-white); }
  .card-front .shapes { position: absolute; inset: 0; }
  .name-tab {
    position: absolute; left: 40px; top: 92px;
    color: #fff; font-family: "Montserrat", sans-serif;
    white-space: nowrap;
  }
  .name-tab .person {
    font-size: 27px; line-height: 1; letter-spacing: .3px;
  }
  .person .first { font-weight: 700; }
  .person .last { font-weight: 500; }
  .name-tab .role {
    margin-top: 7px; font-size: 13px; font-weight: 500; letter-spacing: .5px;
  }
  .card-front .wordmark {
    position: absolute; right: 46px; top: 46px;
    font-family: "Montserrat", sans-serif; font-weight: 600;
    font-size: 24px; line-height: 1.2; letter-spacing: .5px;
    color: var(--brand-blue);
    display: flex; align-items: center; gap: 12px;
  }
  .card-front .wordmark .mark-square { width: 16px; height: 16px; }
  .card-front .wordmark .name { text-align: right; }
  .address {
    position: absolute; right: 46px; top: 150px;
    text-align: right; font-style: normal;
    font-family: "Open Sans", sans-serif; font-size: 16px; line-height: 1.35;
    color: var(--ink-blue);
  }
  .contacts {
    position: absolute; left: 40px; top: 250px;
    font-family: "Open Sans", sans-serif; font-size: 16px; line-height: 1.45;
    color: var(--ink-blue);
    list-style: none;
  }
  .contacts li { display: flex; align-items: center; gap: 12px; }
  .contacts .icon { width: 22px; height: 22px; flex: none; }
  .contacts .no-icon { padding-left: 34px; }
</style>
</head>
<body>
<main class="stage">

  <section class="card card-back" aria-label="Card back">
    <div class="wordmark"><span class="mark-square"></span>GLACIER CLINICAL DISPOSAL</div>
  </section>

  <section class="card card-front" aria-label="Card front">
    <svg class="shapes" width="700" height="400" viewBox="0 0 700 400" aria-hidden="true">
      <polygon points="0,78 372,78 346,150 0,150" fill="var(--brand-blue)"/>
      <polygon points="0,372 560,372 580,354 620,354 640,372 700,372 700,400 0,400" fill="var(--brand-blue)"/>
    </svg>

    <div class="name-tab">
      <div class="person"><span class="first">MARTIN</span> <span class="last">HOLLOWAY</span></div>
      <div class="role">MANAGING DIRECTOR</div>
    </div>

    <div class="wordmark"><span class="mark-square"></span><span class="name">GLACIER CLINICAL<br>DISPOSAL</span></div>

    <address class="address">418 Harbor Ridge Road<br>Ashford WA 98304</address>

    <ul class="contacts">
      <li class="no-icon">555-014-2290</li>
      <li>
        <svg class="icon" viewBox="0 0 22 22" aria-hidden="true"><circle cx="11" cy="11" r="11" fill="var(--icon-grey)"/><path d="M7.5 6.5l2 -0.5 1.2 2.6-1.3 1c.6 1.3 1.6 2.3 2.9 2.9l1-1.3 2.6 1.2-.5 2c-4.4.2-8.1-3.5-7.9-7.9z" fill="#fff"/></svg>
        mholloway@glacierclinical.com
      </li>
      <li>
        <svg class="icon" viewBox="0 0 22 22" aria-hidden="true"><circle cx="11" cy="11" r="11" fill="var(--icon-grey)"/><rect x="5.5" y="7" width="11" height="8" fill="none" stroke="#fff" stroke-width="1.3"/><path d="M5.5 7l5.5 4.5 5.5-4.5" fill="none" stroke="#fff" stroke-width="1.3"/></svg>
        mholloway@glacierclinicaldisposal.com
      </li>
      <li>
        <svg class="icon" viewBox="0 0 22 22" aria-hidden="true"><circle cx="11" cy="11" r="11" fill="var(--icon-grey)"/><g fill="none" stroke="#fff" stroke-width="1.1"><circle cx="11" cy="11" r="5.5"/><ellipse cx="11" cy="11" rx="2.4" ry="5.5"/><path d="M5.5 11h11M6.3 8.3h9.4M6.3 13.7h9.4"/></g></svg>
        www.glacierclinicaldisposal.com
      </li>
    </ul>
  </section>

</main>
</body>
</html>
```